Litigation services brochure for PRV.law

improve aesthetics and sync with website color scheme and new staff to emphasize law firm's litigation capabilities. Describe Litigation director, senior attorneys, attorneys, and general capabilities of the firm, licenses to practice, representative trasnactions and litigation experience. Take profile info from individual attorneys listed in the .doc and correlate with www.prv.law profiles for same attorneys. Update photos as needed. I'm not sure what other words I need to add, but this thing says there needs to be more words in my project description. read the brochure attached, and it should be pretty self explanatory. We have lots of info and content on there, we just want it to look better and reflect the updated color scheme of the site (a few of the color bar colors have changed order and color).

Target Market(s)

Houston, Denver

Font styles to use
Serif

Requirements
Must have
• Color scheme that matches www.prv.law
Nice to have
• Better aesthetics and content optimization

```html
<!DOCTYPE html>
<html lang="en">
<head>
<meta charset="utf-8">
<title>PRV.law — Litigation Brochure</title>
<link rel="stylesheet" href="https://fonts.googleapis.com/css2?family=Cormorant+SC:wght@500;600&family=Oswald:wght@500;600&family=Roboto+Condensed:wght@700&family=Open+Sans:wght@400&display=swap">
<style>
  :root{
    --forest:#1f2b12;
    --forest-text:#24361a;
    --gold:#d1c26c;
    --maroon:#7d1235;
    --cream:#ece6cf;
    --ink:#3a3a3a;
    --paper:#ffffff;
    --backdrop:#f2f2f0;
  }
  *{box-sizing:border-box;margin:0;padding:0}
  html,body{width:1200px;height:1200px;overflow:hidden;background:var(--backdrop)}
  .brochure{position:absolute;left:50px;top:175px;width:1100px;height:850px;background:var(--paper);box-shadow:0 6px 24px rgba(0,0,0,.12);overflow:hidden}
  .brochure-shapes{position:absolute;inset:0}
  .masthead{position:absolute;left:560px;top:18px;width:520px;text-align:center;color:var(--cream)}
  .firm-name{font-family:"Cormorant SC",serif;font-weight:600;font-size:26px;letter-spacing:1px}
  .practice-strip{font-family:"Cormorant SC",serif;font-size:10px;letter-spacing:3px;margin-top:2px}
  .bio{position:absolute;left:40px;top:210px;width:430px;font-family:"Open Sans",sans-serif;color:var(--ink)}
  .bio-name{font-family:"Roboto Condensed",sans-serif;font-weight:700;color:var(--forest-text);font-size:17px;line-height:1.1}
  .bio-text{font-size:9.6px;line-height:1.42;text-align:justify;margin-top:8px}
  .admissions-title{font-family:"Roboto Condensed",sans-serif;font-weight:700;color:var(--forest-text);font-size:17px;margin-top:14px}
  .admissions{font-size:10px;line-height:1.5;margin-top:4px;padding-left:16px}
  .headline{position:absolute;left:690px;top:440px;font-family:"Oswald",sans-serif;font-weight:600;font-size:44px;line-height:1.02;color:var(--forest-text)}
  .headline .accent{color:var(--maroon)}
  .contact{position:absolute;left:650px;top:650px;font-family:"Roboto Condensed",sans-serif;font-weight:700;font-style:normal;color:var(--forest-text);font-size:17px;line-height:1.25}
  .contact-title{margin-bottom:8px}
  .contact-row{display:flex;gap:10px;align-items:flex-start;margin-bottom:6px}
  .contact-row svg{flex:none;margin-top:2px}
</style>
</head>
<body>
<main class="brochure">
  <svg class="brochure-shapes" width="1100" height="850" viewBox="0 0 1100 850">
    <defs>
      <linearGradient id="office" x1="0" y1="0" x2="1" y2="1">
        <stop offset="0" stop-color="#e9f3f4"/><stop offset=".5" stop-color="#b7d4da"/><stop offset="1" stop-color="#7fa3ad"/>
      </linearGradient>
      <linearGradient id="ember" x1="0" y1="0" x2="0" y2="1">
        <stop offset="0" stop-color="#f06a2f"/><stop offset=".6" stop-color="#d9532a"/><stop offset="1" stop-color="#5a2418"/>
      </linearGradient>
      <linearGradient id="wood" x1="0" y1="0" x2="1" y2="1">
        <stop offset="0" stop-color="#e8e8e4"/><stop offset=".5" stop-color="#a98a76"/><stop offset="1" stop-color="#5a3a2c"/>
      </linearGradient>
      <linearGradient id="steel" x1="0" y1="0" x2="1" y2="1">
        <stop offset="0" stop-color="#f2f2ee"/><stop offset="1" stop-color="#9a9a88"/>
      </linearGradient>
    </defs>
    <path class="photo-office" role="img" aria-label="Photo: two professionals shaking hands by office windows" fill="url(#office)"
      d="M470,100 C700,60 900,95 1100,75 V392 C950,402 760,410 640,360 C570,330 520,270 470,200 Z"/>
    <path class="masthead-band" fill="var(--forest)" d="M470,28 C700,4 900,2 1100,0 V78 C900,96 700,62 470,104 Z"/>
    <path class="gold-panel" fill="var(--gold)" d="M640,360 C760,410 950,402 1100,392 V850 H590 C610,700 590,520 640,360 Z"/>
    <path class="divider-curve" fill="none" stroke="var(--forest)" stroke-width="4"
      d="M470,200 C520,270 570,330 640,360 C760,410 950,402 1100,392 M640,360 C590,520 610,700 590,850"/>
    <circle role="img" aria-label="Photo: oil field equipment" cx="520" cy="220" r="40" fill="url(#steel)" stroke="var(--forest)" stroke-width="3"/>
    <circle role="img" aria-label="Photo: gavel on an orange background" cx="645" cy="335" r="75" fill="url(#ember)" stroke="var(--forest)" stroke-width="4"/>
    <circle role="img" aria-label="Photo: wooden gavel on a desk" cx="560" cy="730" r="80" fill="url(#wood)" stroke="var(--forest)" stroke-width="4"/>
  </svg>

  <header class="masthead">
    <div class="firm-name">Parker Reyes &amp; Vance</div>
    <div class="practice-strip">Energy · Intellectual · Corporate · Estates · Litigation</div>
  </header>

  <section class="bio">
    <h2 class="bio-name">Dana H. Collier, J.D.,<br>Senior Counsel &amp; Director of Litigation</h2>
    <p class="bio-text">Dana Collier is Senior Counsel and the Director of Litigation at Parker, Reyes &amp; Vance, PLLC. Dana brings decades of courtroom experience across products liability, energy sector disputes, construction claims, negligence, maritime, employment, and commercial matters in both state and federal courts. Dana is board certified in trial law and has served as national coordinating counsel for several long-standing clients. Dana has represented clients in Texas and in a number of other states, appearing pro hac vice where needed, and holds the top rating from a national peer review directory. Outside the office, Dana volunteers on the board of a local arts nonprofit. Dana has guided clients through complex lost profits claims, wrongful death claims, and serious injury cases, and has defended companies in industrial accident cases involving multiple claimants. Dana has long advised manufacturers and distributors on product safety and claims strategy, and has acted as lead counsel for contractors in multi-party disputes arising from construction incidents at a federal research campus, as well as for energy operators in high-value personal injury and property damage claims arising from offshore incidents. Dana's experience on both the plaintiff and defense sides of high stakes, complicated trials provides lasting value to clients in shaping trial strategy and developing litigation talent across the firm.<br>Dana Collier is admitted to practice before the United States District Courts for the Northern, Southern, and Eastern Districts of Texas, all State Courts of Texas, the United States Courts of Appeal for the Fifth and Federal Circuits, the United States Court of Federal Claims, and the Supreme Court of the United States. Dana is based in the Houston, Texas, office of Parker, Reyes &amp; Vance, PLLC.</p>
    <h3 class="admissions-title">ADMISSIONS TO PRACTICE</h3>
    <ul class="admissions">
      <li>Texas</li>
      <li>U.S. Northern, Eastern, and Southern Districts of Texas</li>
      <li>U.S. Court of Federal Claims</li>
      <li>U.S. 5th Circuit Court of Appeals, and the U.S. Supreme Court</li>
    </ul>
  </section>

  <h1 class="headline">
    <span>ENERGY</span><br>
    <span class="accent">INTELLECTUAL</span><br>
    <span>CORPORATE, ESTATES</span><br>
    <span class="accent">LITIGATION</span>
  </h1>

  <address class="contact">
    <div class="contact-title">Contact Us</div>
    <div class="contact-row">
      <svg width="16" height="16" viewBox="0 0 24 24" aria-hidden="true"><path fill="var(--forest)" d="M6.6 10.8a15.2 15.2 0 0 0 6.6 6.6l2.2-2.2c.3-.3.7-.4 1-.2 1.1.4 2.300.6 3.6.6.6 0 1 .4 1 1V20c0 .6-.4 1-1 1A17 17 0 0 1 3 4c0-.6.4-1 1-1h3.5c.6 0 1 .4 1 1 0 1.3.2 2.5.6 3.6.1.3 0 .7-.2 1z"/></svg>
      <span>(713) 555-0148</span>
    </div>
    <div class="contact-row">
      <svg width="16" height="18" viewBox="0 0 24 24" aria-hidden="true"><path fill="var(--forest)" d="M12 2a7 7 0 0 0-7 7c0 5.2 7 13 7 13s7-7.8 7-13a7 7 0 0 0-7-7zm0 9.5A2.5 2.5 0 1 1 12 6.5a2.5 2.5 0 0 1 0 5z"/></svg>
      <span>Bayou Commerce Center,<br>220 Travis Ln., Suite 310,<br>Houston, TX 77002</span>
    </div>
  </address>
</main>
</body>
</html>
```